I need a full PowerPoint template (with multiple slide options) for a new imaging center company - Brightwell Medical Imaging. I have attached the Logo and Brand Identity here.

```html
<!DOCTYPE html>
<html lang="en">
<head>
<meta charset="utf-8">
<title>Brightwell Medical Imaging – Presentation Template</title>
<link rel="stylesheet" href="https://fonts.googleapis.com/css2?family=Montserrat:wght@700;800&family=Inter:wght@300;400;500;600;700&display=swap">
<style>
  :root{
    --board:#88898d;
    --navy:#0d3a75;
    --ink-navy:#16305e;
    --deep:#15144a;
    --blue:#1f6cc6;
    --blue-soft:#d9e8f7;
    --green:#1d8a3c;
    --panel:#e9ecf1;
    --text:#222630;
    --muted:#4b505a;
    --rule:#b9bdc6;
    --white:#ffffff;
  }
  *{box-sizing:border-box;margin:0;padding:0}
  html,body{width:1017px;height:1200px;overflow:hidden;background:var(--board)}
  body{font-family:"Inter",sans-serif;color:var(--text)}
  .canvas{position:relative;width:1017px;height:1200px;background:var(--board)}
  .slide{position:absolute;width:460px;height:258px;background:var(--white);overflow:hidden}
  .abs{position:absolute}
  .photo{position:absolute}

  /* brand lockup */
  .brand{position:absolute;display:flex;align-items:center;gap:5px;color:var(--ink-navy);font-family:"Montserrat",sans-serif;font-weight:700}
  .brand-dot{width:18px;height:18px;border-radius:50%;background:var(--blue);flex:none}
  .brand-name{display:flex;flex-direction:column;line-height:1}
  .brand-name .main{font-size:10px;letter-spacing:.2px}
  .brand-name .sub{font-size:4.6px;letter-spacing:.6px;margin-top:2px}
  .slide-head .brand{left:9px;top:11px}

  .tag{position:absolute;left:116px;top:10.4px;height:21px;padding:0 7px;background:var(--navy);color:var(--white);
       font-family:"Montserrat",sans-serif;font-weight:800;font-size:12.5px;line-height:21px;letter-spacing:.2px;white-space:nowrap}

  /* slide 1 */
  .cover .brand{left:27px;top:34px;gap:7px}
  .cover .brand-dot{width:32px;height:32px}
  .cover .brand-name .main{font-size:17px}
  .cover .brand-name .sub{font-size:7.6px;margin-top:3px;letter-spacing:1px}
  .cover-title{position:absolute;left:27px;top:86px;font-family:"Montserrat",sans-serif;font-weight:800;line-height:1}
  .cover-title .l1,.cover-title .l2{display:block;color:var(--blue);font-size:25px;margin-bottom:7px}
  .cover-title .l3{display:block;color:var(--green);font-size:17px}
  .tagline{position:absolute;left:28px;top:181px;font-size:11.5px;line-height:16px;color:#2a2e36}

  /* slide 2 agenda */
  .agenda-col{position:absolute;top:37px}
  .agenda-item{position:relative;height:30.5px;border-bottom:1px solid var(--rule);padding-top:5.5px}
  .agenda-item .t{font-size:6.8px;font-weight:600;color:#1b1f27;line-height:1.2}
  .agenda-item .s{font-size:5.3px;color:var(--muted);margin-top:1.5px}
  .agenda-item .num{position:absolute;right:6px;top:7px;width:14px;height:14px;border-radius:50%;background:var(--green);
       color:var(--white);font-size:5.3px;font-weight:700;display:flex;align-items:center;justify-content:center}

  /* slide 3 */
  .about-text{position:absolute;left:22px;top:55px;width:165px;font-size:7.2px;line-height:12px;text-align:justify;color:#2a2e36}
  .feature-box{position:absolute;left:22px;top:146.5px;width:152px;height:85px;background:var(--panel);border-radius:5px;padding:11px 0 0 14px}
  .ticks{list-style:none}
  .ticks li{position:relative;padding-left:12px;font-size:7.2px;color:#2a2e36;line-height:17.3px}
  .ticks li::before{content:"";position:absolute;left:0;top:6px;width:5px;height:5px;border-radius:50%;background:var(--green)}

  /* slide 4 */
  .apart-panel{position:absolute;left:10px;top:50.7px;width:437px;height:192px;background:var(--panel);border-radius:5px;overflow:hidden}
  .apart-list{position:absolute;left:202px;top:14px}
  .apart-list li{line-height:17.3px}

  /* slide 5 */
  .services{position:absolute;left:0;top:47px;width:460px;height:211px;background:var(--deep);border-radius:5px 5px 0 0}
  .service{position:absolute;top:0;width:86px;color:var(--white)}
  .service svg{position:absolute;top:15px}
  .service h3{position:absolute;top:79px;font-family:"Montserrat",sans-serif;font-weight:800;font-size:10.5px;letter-spacing:.2px;white-space:nowrap}
  .service p{position:absolute;top:96px;width:84px;font-size:5.7px;line-height:7.2px;color:#d7d9ea}

  /* slide 6 */
  .chart-note{position:absolute;left:259px;top:20px;font-family:"Montserrat",sans-serif;font-weight:800;font-size:8.3px;line-height:14.5px;color:var(--navy)}
  .chart-copy{position:absolute;left:331px;width:112px;font-size:5.5px;line-height:7.6px;color:#2a2e36}

  /* slide 7 */
  .step-label{position:absolute;width:90px;text-align:center;font-family:"Inter",sans-serif;font-weight:600;font-size:6.8px;line-height:8.5px;color:var(--ink-navy)}
  .step-copy{position:absolute;width:92px;text-align:center;font-size:5.4px;line-height:7.7px;color:#2a2e36}

  /* slide 8 */
  .closing{background:#0f1e4f}
  .closing .brand{left:128px;top:34px;gap:9px;color:var(--white)}
  .closing .brand-dot{width:46px;height:46px}
  .closing .brand-name .main{font-size:27px}
  .closing .brand-name .sub{font-size:11px;margin-top:4px;letter-spacing:1.4px;text-align:center}
  .closing .rule{position:absolute;left:133px;width:197px;height:1px;background:#2c5aa8}
  .thanks{position:absolute;left:0;right:0;top:135px;text-align:center;font-family:"Inter",sans-serif;font-weight:300;font-size:31px;color:#2777d4}
</style>
</head>
<body>
<div class="canvas">

  <!-- 1 · Cover -->
  <section class="slide cover" style="left:37.5px;top:39px">
    <svg class="photo" width="460" height="258" viewBox="0 0 460 258" role="img" aria-label="Photo of a white MRI scanner ring with a control screen, in soft blue light">
      <defs>
        <linearGradient id="coverPhoto" x1="0" y1="0" x2="1" y2="1">
          <stop offset="0" stop-color="#c9d9e7"/>
          <stop offset=".5" stop-color="#e6eef5"/>
          <stop offset="1" stop-color="#9fb7cc"/>
        </linearGradient>
      </defs>
      <rect width="460" height="258" fill="url(#coverPhoto)"/>
      <path d="M0 0 H235 C275 60 278 180 194 258 H0 Z" fill="#ffffff"/>
    </svg>
    <div class="brand"><span class="brand-dot"></span><span class="brand-name"><span class="main">BRIGHTWELL</span><span class="sub">— MEDICAL IMAGING —</span></span></div>
    <h1 class="cover-title"><span class="l1">BRIGHTWELL</span><span class="l2">MEDICAL</span><span class="l3">IMAGING</span></h1>
    <p class="tagline">Precision Diagnostics.<br>Clear Decisions.</p>
  </section>

  <!-- 2 · Agenda -->
  <section class="slide slide-head" style="left:521px;top:38px">
    <div class="brand"><span class="brand-dot"></span><span class="brand-name"><span class="main">BRIGHTWELL</span><span class="sub">— MEDICAL IMAGING —</span></span></div>
    <div class="tag">AGENDA</div>
    <div class="agenda-col" style="left:11.5px;width:148px">
      <div class="agenda-item"><div class="t">Lorem Ipsum</div><div class="s">Contrary to popular belief</div><span class="num">01</span></div>
      <div class="agenda-item"><div class="t">Lorem Ipsum</div><div class="s">Contrary to popular belief</div><span class="num">02</span></div>
      <div class="agenda-item"><div class="t">Lorem Ipsum</div><div class="s">Contrary to popular belief</div><span class="num">03</span></div>
      <div class="agenda-item"><div class="t">Lorem Ipsum</div><div class="s">Contrary to popular belief</div><span class="num">04</span></div>
      <div class="agenda-item"><div class="t">Lorem Ipsum</div><div class="s">Contrary to popular belief</div><span class="num">05</span></div>
      <div class="agenda-item"><div class="t">Lorem Ipsum</div><div class="s">Contrary to popular belief</div><span class="num">06</span></div>
      <div class="agenda-item"><div class="t">Lorem Ipsum</div><div class="s">Contrary to popular belief</div><span class="num">07</span></div>
    </div>
    <div class="agenda-col" style="left:172px;width:120px">
      <div class="agenda-item"><div class="t">Lorem Ipsum</div><div class="s">Contrary to popular belief</div><span class="num">08</span></div>
      <div class="agenda-item"><div class="t">Lorem Ipsum</div><div class="s">Contrary to popular belief</div><span class="num">09</span></div>
      <div class="agenda-item"><div class="t">Lorem Ipsum</div><div class="s">Contrary to popular belief</div><span class="num">10</span></div>
      <div class="agenda-item"><div class="t">Lorem Ipsum</div><div class="s">Contrary to popular belief</div><span class="num">11</span></div>
      <div class="agenda-item"><div class="t">Lorem Ipsum</div><div class="s">Contrary to popular belief</div><span class="num">12</span></div>
      <div class="agenda-item"><div class="t">Lorem Ipsum</div><div class="s">Contrary to popular belief</div><span class="num">13</span></div>
      <div class="agenda-item"><div class="t">Lorem Ipsum</div><div class="s">Contrary to popular belief</div><span class="num">14</span></div>
    </div>
    <svg class="photo" style="left:306px;top:0" width="154" height="258" role="img" aria-label="Photo of a radiologist seen from behind, seated before monitors and a glowing scanner">
      <defs>
        <radialGradient id="agendaPhoto" cx=".5" cy=".2" r=".9">
          <stop offset="0" stop-color="#9ee3f5"/>
          <stop offset=".4" stop-color="#3f7fa6"/>
          <stop offset="1" stop-color="#173150"/>
        </radialGradient>
      </defs>
      <rect width="154" height="258" fill="url(#agendaPhoto)"/>
    </svg>
  </section>

  <!-- 3 · Who we are -->
  <section class="slide slide-head" style="left:37.5px;top:318px">
    <svg class="abs" width="460" height="258"><polygon points="294,0 460,0 460,258 343,258" fill="var(--blue-soft)"/></svg>
    <div class="brand"><span class="brand-dot"></span><span class="brand-name"><span class="main">BRIGHTWELL</span><span class="sub">— MEDICAL IMAGING —</span></span></div>
    <div class="tag">WHO WE ARE</div>
    <p class="about-text">Brightwell Medical Imaging is a modern diagnostic imaging center dedicated to delivering accurate, timely, and patient-focused diagnostic services. We combine advanced imaging technology with experienced radiology professionals to support confident medical decisions.</p>
    <div class="feature-box">
      <ul class="ticks">
        <li>Advanced imaging technology</li>
        <li>Skilled radiologists &amp; technicians</li>
        <li>Patient-first approach</li>
        <li>Fast, reliable reporting</li>
      </ul>
    </div>
    <svg class="abs" width="460" height="258">
      <defs>
        <linearGradient id="aboutPhoto" x1="0" y1="0" x2="1" y2="1">
          <stop offset="0" stop-color="#8fb6dc"/>
          <stop offset=".55" stop-color="#dfe7ef"/>
          <stop offset="1" stop-color="#5e7fa3"/>
        </linearGradient>
      </defs>
      <g fill="none" stroke-width="11">
        <circle cx="330.6" cy="130.4" r="104" stroke="var(--blue)" stroke-dasharray="245 409" transform="rotate(165 330.6 130.4)"/>
        <circle cx="330.6" cy="130.4" r="104" stroke="var(--green)" stroke-dasharray="160 494" transform="rotate(332 330.6 130.4)"/>
        <circle cx="330.6" cy="130.4" r="104" stroke="var(--deep)" stroke-dasharray="140 514" transform="rotate(77 330.6 130.4)"/>
      </g>
      <circle cx="330.6" cy="130.4" r="96" fill="url(#aboutPhoto)" role="img" aria-label="Photo of an ultrasound machine with its screen and control panel"/>
    </svg>
  </section>

  <!-- 4 · What sets us apart -->
  <section class="slide slide-head" style="left:520px;top:322px">
    <div class="brand"><span class="brand-dot"></span><span class="brand-name"><span class="main">BRIGHTWELL</span><span class="sub">— MEDICAL IMAGING —</span></span></div>
    <div class="tag">WHAT SETS US APART</div>
    <div class="apart-panel">
      <svg class="photo" width="174" height="192" role="img" aria-label="Photo of a technician preparing a patient lying on a CT scanner table">
        <defs>
          <linearGradient id="apartPhoto" x1="0" y1="0" x2="1" y2="1">
            <stop offset="0" stop-color="#c7d3de"/>
            <stop offset=".5" stop-color="#eef2f6"/>
            <stop offset="1" stop-color="#a9b9c8"/>
          </linearGradient>
        </defs>
        <rect width="174" height="192" fill="url(#apartPhoto)"/>
      </svg>
      <ul class="ticks apart-list">
        <li>High-resolution imaging with latest-generation equipment</li>
        <li>Accurate reporting by experienced radiologists</li>
        <li>Minimal wait times &amp; efficient workflows</li>
        <li>Comfortable, patient-friendly environment</li>
        <li>Strict quality &amp; safety protocols</li>
        <li>Lorem ipsum dolor sit amet, consectetur</li>
        <li>Sed ut perspiciatis unde omnis iste natus error sit volupta</li>
        <li>But I must explain to you how all this mis</li>
        <li>At vero eos et accusamus et iusto odio</li>
      </ul>
    </div>
  </section>

  <!-- 5 · Our services -->
  <section class="slide slide-head" style="left:37.5px;top:605px">
    <div class="brand"><span class="brand-dot"></span><span class="brand-name"><span class="main">BRIGHTWELL</span><span class="sub">— MEDICAL IMAGING —</span></span></div>
    <div class="tag">OUR SERVICES</div>
    <div class="services">
      <div class="service" style="left:20.5px">
        <svg style="left:0" width="48" height="48" viewBox="0 0 48 48">
          <circle cx="24" cy="24" r="22" fill="none" stroke="var(--blue)" stroke-width="4" stroke-dasharray="80 60" transform="rotate(180 24 24)"/>
          <circle cx="24" cy="24" r="22" fill="none" stroke="var(--green)" stroke-width="4" stroke-dasharray="40 100" transform="rotate(20 24 24)"/>
          <circle cx="24" cy="24" r="18" fill="#fff"/>
          <g fill="none" stroke="var(--deep)" stroke-width="1.6"><circle cx="24" cy="23" r="9"/><circle cx="24" cy="23" r="5"/><path d="M15 33h18"/></g>
        </svg>
        <h3>MRI</h3>
        <p>Sed ut perspiciatis unde omnis iste natus error sit voluptatem accusantium doloremque laudantium, totam rem aperiam, eaq ue ipsa quae ab illo inven tore veritatis et quasi architecto beatae vitae dicta sunt explicabo. Nemo enim ipsam volu ptatem quia voluptas sit aspernatur aut odit aut fugit,tore veritatis et quasi architecto beatae vitae dicta sunt explicabo.</p>
      </div>
      <div class="service" style="left:127px">
        <svg style="left:0" width="48" height="48" viewBox="0 0 48 48">
          <circle cx="24" cy="24" r="22" fill="none" stroke="var(--blue)" stroke-width="4" stroke-dasharray="80 60" transform="rotate(180 24 24)"/>
          <circle cx="24" cy="24" r="22" fill="none" stroke="var(--green)" stroke-width="4" stroke-dasharray="40 100" transform="rotate(20 24 24)"/>
          <circle cx="24" cy="24" r="18" fill="#fff"/>
          <g fill="none" stroke="var(--deep)" stroke-width="1.6"><path d="M22 14a9 9 0 1 1 0 18"/><circle cx="24" cy="23" r="4"/><path d="M14 27h10"/></g>
        </svg>
        <h3>CT SCAN</h3>
        <p>Sed ut perspiciatis unde omnis iste natus error sit voluptatem accusantium doloremque laudantium, totam rem aperiam, eaq ue ipsa quae ab illo inven tore veritatis et quasi architecto beatae vitae dicta sunt explicabo. Nemo enim ipsam volu ptatem quia voluptas sit aspernatur aut odit aut fugit,tore veritatis et quasi architecto beatae vitae dicta sunt explicabo.</p>
      </div>
      <div class="service" style="left:240.7px">
        <svg style="left:0" width="48" height="48" viewBox="0 0 48 48">
          <circle cx="24" cy="24" r="22" fill="none" stroke="var(--blue)" stroke-width="4" stroke-dasharray="80 60" transform="rotate(180 24 24)"/>
          <circle cx="24" cy="24" r="22" fill="none" stroke="var(--green)" stroke-width="4" stroke-dasharray="40 100" transform="rotate(20 24 24)"/>
          <circle cx="24" cy="24" r="18" fill="#fff"/>
          <g fill="none" stroke="var(--deep)" stroke-width="1.6"><rect x="16" y="14" width="16" height="19" rx="1.5"/><path d="M24 16v15M20 20h8M20 24h8M20 28h8"/></g>
        </svg>
        <h3>DIGITAL X-RAY</h3>
        <p>Sed ut perspiciatis unde omnis iste natus error sit voluptatem accusantium doloremque laudantium, totam rem aperiam, eaq ue ipsa quae ab illo inven tore veritatis et quasi architecto beatae vitae dicta sunt explicabo. Nemo enim ipsam volu ptatem quia voluptas sit aspernatur aut odit aut fugit, Sed ut perspiciatis unde omnis iste natus error sit voluptatem accusantium doloremque laudantium, totam rem aperiam, eaq ue ipsa quae ab illo</p>
      </div>
      <div class="service" style="left:356.6px">
        <svg style="left:0" width="48" height="48" viewBox="0 0 48 48">
          <circle cx="24" cy="24" r="22" fill="none" stroke="var(--blue)" stroke-width="4" stroke-dasharray="80 60" transform="rotate(180 24 24)"/>
          <circle cx="24" cy="24" r="22" fill="none" stroke="var(--green)" stroke-width="4" stroke-dasharray="40 100" transform="rotate(20 24 24)"/>
          <circle cx="24" cy="24" r="18" fill="#fff"/>
          <g fill="none" stroke="var(--deep)" stroke-width="1.6"><path d="M17 31l8-8 4 4-8 8z"/><path d="M25 23l4-6 6 6-6 4"/><path d="M31 14a5 5 0 0 1 5 5"/></g>
        </svg>
        <h3>ULTRASOUND</h3>
        <p>Sed ut perspiciatis unde omnis iste natus error sit voluptatem accusantium doloremque laudantium, totam rem aperiam, eaq ue ipsa quae ab illo inven tore veritatis et quasi architecto beatae vitae dicta sunt explicabo. Nemo enim ipsam volu ptatem quia voluptas sit aspernatur aut odit aut fugit, Sed ut perspiciatis unde omnis iste natus error sit voluptatem accusantium doloremque laudantium, totam rem aperiam,</p>
      </div>
    </div>
  </section>

  <!-- 6 · Chart -->
  <section class="slide slide-head" style="left:517px;top:609px">
    <svg class="abs" width="460" height="258">
      <polygon points="221,0 460,0 460,258 281,258" fill="#e8edf5"/>
      <rect x="0" y="67.5" width="316.5" height="163.5" fill="#fff"/>
    </svg>
    <div class="brand"><span class="brand-dot"></span><span class="brand-name"><span class="main">BRIGHTWELL</span><span class="sub">— MEDICAL IMAGING —</span></span></div>
    <div class="tag">HEADING</div>
    <p class="chart-note">LOREM IPSUM DOLOR SIT AMET, CO<br>NSECTETUR ADIPISCING ELIT.</p>
    <svg class="abs" width="320" height="258" font-family="Inter, sans-serif" font-size="7" fill="#333">
      <g stroke="#4bb3a3" stroke-width=".7">
        <line x1="35.2" y1="87" x2="303.3" y2="87"/>
        <line x1="35.2" y1="111.3" x2="303.3" y2="111.3"/>
        <line x1="35.2" y1="135.5" x2="303.3" y2="135.5"/>
        <line x1="35.2" y1="159.7" x2="303.3" y2="159.7"/>
        <line x1="35.2" y1="184" x2="303.3" y2="184"/>
      </g>
      <g stroke="#f2c46b" stroke-width=".7">
        <line x1="59.4" y1="192" x2="59.4" y2="204.7"/>
        <line x1="84.2" y1="160.3" x2="84.2" y2="204.7"/>
        <line x1="108.4" y1="139.5" x2="108.4" y2="204.7"/>
        <line x1="132.7" y1="137.8" x2="132.7" y2="204.7"/>
        <line x1="156.9" y1="115.3" x2="156.9" y2="204.7"/>
        <line x1="181" y1="126.3" x2="181" y2="204.7"/>
        <line x1="205.3" y1="103.2" x2="205.3" y2="204.7"/>
        <line x1="229.5" y1="129.7" x2="229.5" y2="204.7"/>
        <line x1="253.7" y1="106.1" x2="253.7" y2="204.7"/>
        <line x1="277.9" y1="91.1" x2="277.9" y2="204.7"/>
      </g>
      <polyline points="35.2,204.7 59.4,192 84.2,160.3 108.4,139.5 132.7,137.8 156.9,115.3 181,126.3 205.3,103.2 229.5,129.7 253.7,106.1 277.9,91.1" fill="none" stroke="#8b2a86" stroke-width="1.3"/>
      <path d="M35.2 59 V204.7 H303.3" fill="none" stroke="#222" stroke-width="1.4"/>
      <g text-anchor="end">
        <text x="25" y="89.5">100</text><text x="25" y="113.8">80</text><text x="25" y="138">60</text><text x="25" y="162.2">40</text><text x="25" y="186.5">20</text>
      </g>
      <g text-anchor="middle">
        <text x="25.5" y="219">0</text><text x="59.4" y="219">10</text><text x="84.2" y="219">20</text><text x="108.4" y="219">30</text><text x="132.7" y="219">40</text><text x="156.9" y="219">50</text><text x="181" y="219">60</text><text x="205.3" y="219">70</text><text x="229.5" y="219">80</text><text x="253.7" y="219">90</text><text x="279" y="219">100</text>
      </g>
    </svg>
    <p class="chart-copy" style="top:82px">Lorem ipsum dolor sit amet, consectetur adipiscing elit, sed do eiusmod tempor incididunt ut labore et dolore magna aliqua. Ut enim ad minim veniam, quis nostrud exercitation ullamco laboris nisi ut aliquip ex ea commodo consequat. Duis aute irure dolor in reprehenderit in voluptate velit esse cillum</p>
    <p class="chart-copy" style="top:158px">Lorem ipsum dolor sit amet, consectetur adipiscing elit, sed do eiusmod tempor incididunt ut labore et dolore magna aliqua. Ut enim ad minim veniam, quis nostrud exercitation ullamco laboris nisi ut aliquip ex ea commodo consequat. Duis aute irure dolor in reprehenderit in voluptate velit esse cillum</p>
  </section>

  <!-- 7 · Process -->
  <section class="slide slide-head" style="left:38.6px;top:891px">
    <div class="brand"><span class="brand-dot"></span><span class="brand-name"><span class="main">BRIGHTWELL</span><span class="sub">— MEDICAL IMAGING —</span></span></div>
    <div class="tag">HEADING</div>
    <svg class="abs" width="460" height="258">
      <defs>
        <clipPath id="upper"><rect x="0" y="0" width="460" height="128"/></clipPath>
        <clipPath id="lower"><rect x="0" y="82" width="460" height="176"/></clipPath>
        <filter id="lift" x="-20%" y="-20%" width="140%" height="140%"><feDropShadow dx="0" dy="2" stdDeviation="2" flood-color="#0d2a55" flood-opacity=".35"/></filter>
      </defs>
      <polygon clip-path="url(#upper)" fill="#4f93c6" points="75.4,45 132.4,76.5 132.4,139.5 75.4,171 18.4,139.5 18.4,76.5"/>
      <polygon clip-path="url(#lower)" fill="#3e7fb8" points="178,45 235,76.5 235,139.5 178,171 121,139.5 121,76.5"/>
      <polygon clip-path="url(#upper)" fill="#2f62a0" points="279.5,45 336.5,76.5 336.5,139.5 279.5,171 222.5,139.5 222.5,76.5"/>
      <polygon clip-path="url(#lower)" fill="#1f4a86" points="380.4,45 437.4,76.5 437.4,139.5 380.4,171 323.4,139.5 323.4,76.5"/>
      <g fill="#fff" filter="url(#lift)">
        <polygon points="75.4,54 118.4,81 118.4,135 75.4,162 32.4,135 32.4,81"/>
        <polygon points="178,54 221,81 221,135 178,162 135,135 135,81"/>
        <polygon points="279.5,54 322.5,81 322.5,135 279.5,162 236.5,135 236.5,81"/>
        <polygon points="380.4,54 423.4,81 423.4,135 380.4,162 337.4,135 337.4,81"/>
      </g>
      <g fill="none" stroke="var(--ink-navy)" stroke-width="1.1">
        <rect x="67" y="86" width="17" height="13" rx="1"/><path d="M67 91h17M73 94h5M70 82h11v4"/>
        <rect x="170" y="82" width="15" height="18" rx="1"/><circle cx="176" cy="93" r="4"/><path d="M179 96l4 4M173 86h8"/>
        <rect x="272" y="82" width="13" height="17" rx="1"/><path d="M275 87h7M275 91h7M275 95h4"/><circle cx="286" cy="96" r="3.5"/>
        <circle cx="380" cy="91" r="6"/><path d="M380 85v-4M376 87l-3-3M384 87l3-3M377 97v3h6v-3"/>
      </g>
    </svg>
    <div class="step-label" style="left:30.4px;top:119px">DOCUMENTS<br>ARRIVE</div>
    <div class="step-label" style="left:133px;top:123px">AI ANALYSIS</div>
    <div class="step-label" style="left:234.5px;top:119px">VALIDATED<br>SUGGESTIONS</div>
    <div class="step-label" style="left:335.4px;top:123px">YOU DECIDE</div>
    <p class="step-copy" style="left:29.4px;top:172px">Sed ut perspiciatis unde omnis iste natus error sit voluptatem accusantium doloremque laudantium, totam rem aperiam, eaque ipsa quae ab illo inventore veritatis et quasi architecto beatae vitae dicta sunt explicabo sed quia consequuntur magni dolores eos qui ratione voluptatem</p>
    <p class="step-copy" style="left:132px;top:187px">Sed ut perspiciatis unde omnis iste natus error sit voluptatem accusantium doloremque laudantium, totam rem aperiam, eaque ipsa quae ab illo inventore veritatis et quasi architecto beatae vitae dicta sunt explicabo sed quia consequuntu.</p>
    <p class="step-copy" style="left:233.5px;top:172px">Sed ut perspiciatis unde omnis iste natus error sit voluptatem accusantium doloremque laudantium, totam rem aperiam, eaque ipsa quae ab illo inventore veritatis et quasi architecto beatae vitae dicta sunt explicabo sed quia consequuntur magni dolores eos qui ratione voluptatem</p>
    <p class="step-copy" style="left:334.4px;top:187px">Sed ut perspiciatis unde omnis iste natus error sit voluptatem accusantium doloremque laudantium, totam rem aperiam, eaque ipsa quae ab illo inventore veritatis et quasi architecto beatae vitae dicta sunt explicabo sed quia consequuntu.</p>
  </section>

  <!-- 8 · Closing -->
  <section class="slide closing" style="left:515.5px;top:894px">
    <svg class="photo" width="460" height="258" role="img" aria-label="Faint background photo of an MRI scanner under a dark blue tint">
      <defs>
        <radialGradient id="closingPhoto" cx=".55" cy=".6" r=".7">
          <stop offset="0" stop-color="#1d3470"/>
          <stop offset=".6" stop-color="#132556"/>
          <stop offset="1" stop-color="#0c1a45"/>
        </radialGradient>
      </defs>
      <rect width="460" height="258" fill="url(#closingPhoto)"/>
    </svg>
    <div class="brand"><span class="brand-dot"></span><span class="brand-name"><span class="main">BRIGHTWELL</span><span class="sub">— MEDICAL IMAGING —</span></span></div>
    <div class="rule" style="top:124px"></div>
    <p class="thanks">Thank You</p>
    <div class="rule" style="top:186px"></div>
  </section>

</div>
</body>
</html>
```